Dog care service needs advertising poster

Our company is Paw Haven. We provide care for dogs while their owners are away, either through home visits or a holiday stay in the homes of carefully selected minders. Our existing website & Facebook cover should provide all the colour cues for a poster - namely blues, blondes and grey. We have an existing logo (provided). We can feature the same imagery from our website as I have purchased the rights to the stock images.

www.pawhavenexample.com.au
www.facebook.com/pawhavenexampleau

This brief is for design of a poster that can be placed in vet surgeries, groomers, on community noticeboards. It should be scalable to print in three sizes, A5, A4 & A3.

We wish to clearly communicate our three areas of service "dog minding, home visits, dog walking".

We would like to have the files ready for upload to Printora (or similar) for immediate printing.

Target Market(s)

Dog owners who love their dogs like family.

Industry/Entity Type

Advertising

Font styles to use
Sans Serif

Colors
33a6d7
3276b5

Requirements
Must have
• Logo
• www.pawhavenexample.com.au
• Telephone number
• Three services - Dog Minding, Home Visits, Dog Walking
Nice to have
• use of our existing stock photography to highlight the three areas of service - Dog minding, home visits, dog walking. Existing colour palette - blues, blondes and grey.
• Text that can be used:
• Western Sydney’s complete dog care service.
• Dog Minding - Your dog stays in the home of one of our carefully selected minders.Treated like part of the family, they enjoy all the creature comforts they are used to.
• Home Visits - We visit your dog at your home for feeding, walking and playtime. Short of long visits available.
• Dog Walking - If you can't walk your dog for any reason we are here to help. 1/2 hour or hourly walks available.
• Contact us today for a tailored package to meet your needs.
Should not have
• Any additional illustrations beyond the logo.

```html
<!DOCTYPE html>
<html lang="en">
<head>
<meta charset="utf-8">
<title>Paw Haven Pet Services – Poster</title>
<link rel="stylesheet" href="https://fonts.googleapis.com/css2?family=Nunito:wght@700;800;900&family=Varela+Round&family=Open+Sans:wght@400;600&display=swap">
<style>
  :root {
    --brand-grey: #3c4657;
    --brand-sky: #33a6d7;
    --brand-blue: #3276b5;
    --deep-blue: #1d4f9a;
    --navy: #1f3a82;
    --ink-navy: #25376b;
    --sun-yellow: #ffeb1a;
    --alert-red: #e4232a;
    --white: #ffffff;
  }
  * { margin: 0; padding: 0; box-sizing: border-box; }
  html, body { width: 848px; height: 1200px; overflow: hidden; background: var(--white); }
  .poster {
    position: relative; width: 848px; height: 1200px; overflow: hidden;
    background: var(--white); font-family: "Open Sans", Arial, sans-serif;
  }

  /* Brand header */
  .brand { position: absolute; left: 128px; top: 38px; display: flex; align-items: center; gap: 26px; }
  .brand-dot { width: 120px; height: 120px; border-radius: 50%; background: var(--brand-grey); }
  .brand-name {
    font-family: "Varela Round", sans-serif; font-size: 66px; line-height: 1;
    color: var(--brand-grey);
  }
  .brand-tag {
    font-family: "Varela Round", sans-serif; font-size: 20px; letter-spacing: 7px;
    color: var(--brand-sky); margin-top: 14px; padding-left: 40px;
  }

  /* Hero photograph area */
  .hero-photo {
    position: absolute; left: 0; top: 246px; width: 848px; height: 400px;
    background: linear-gradient(180deg, #cfdde6 0%, #b9d0df 30%, #4f8fb5 38%, #2f6f9c 60%, #5b8fb0 78%, #d8c5a2 86%, #cdb48c 100%);
  }

  /* Blue information panel */
  .info-panel {
    position: absolute; left: 0; top: 560px; width: 848px; height: 526px;
    background: linear-gradient(180deg, rgba(76,178,230,0) 0%, #4ab2e6 14%, #3a9bd9 38%, #2a78c4 70%, #1d56a3 100%);
  }

  /* Headline: all white outlines drawn first, then all letter fills on top */
  .headline { position: absolute; left: 20px; top: 500px; width: 560px; height: 280px; }
  .headline-word { font-family: "Nunito", sans-serif; font-weight: 900; }
  .headline-word.small { font-weight: 800; }
  .headline-outline use { fill: var(--white); stroke: var(--white); stroke-width: 16px; stroke-linejoin: round; }
  .headline-fill .big { fill: var(--brand-blue); }
  .headline-fill .small { fill: var(--brand-sky); }

  .tagline {
    position: absolute; left: 50px; top: 793px; font-family: "Nunito", sans-serif;
    font-weight: 800; font-size: 24.5px; color: var(--sun-yellow); white-space: nowrap;
  }

  .services { position: absolute; left: 98px; top: 846px; width: 500px; }
  .service { display: flex; color: var(--white); margin-bottom: 14px; }
  .service-name { width: 147px; font-family: "Nunito", sans-serif; font-weight: 700; font-size: 16px; white-space: nowrap; }
  .service-text { font-size: 11.5px; line-height: 1.25; width: 325px; padding-top: 2px; font-weight: 600; }

  .burst { position: absolute; left: 66px; top: 980px; width: 180px; height: 160px; }
  .burst-text { font-family: "Nunito", sans-serif; font-weight: 800; font-size: 14.5px; fill: var(--white); }

  .call { position: absolute; left: 280px; top: 1006px; width: 290px; text-align: center; }
  .call-lead { font-family: "Nunito", sans-serif; font-weight: 700; font-size: 17px; color: var(--white); }
  .call-phone { font-family: "Nunito", sans-serif; font-weight: 900; font-size: 38px; color: var(--sun-yellow); line-height: 1.1; letter-spacing: 1px; }

  .web-links { position: absolute; right: 48px; top: 1086px; text-align: right; }
  .web-link { font-family: "Nunito", sans-serif; font-weight: 800; font-size: 27px; color: var(--ink-navy); line-height: 1.18; }
  .footer-band { position: absolute; left: 0; bottom: 0; width: 848px; height: 34px; background: var(--navy); }

  /* Service photo badges */
  .service-badge { position: absolute; left: 606px; width: 248px; height: 290px; }
  .badge-photo {
    position: absolute; left: 2px; top: 0; width: 236px; height: 236px; border-radius: 50%;
    border: 6px solid var(--white); box-shadow: 0 0 0 4px var(--navy);
  }
  .badge-ribbon {
    position: absolute; left: 36px; top: 232px; width: 240px; height: 46px;
    background: var(--navy); transform: rotate(-16deg); transform-origin: left center;
    color: var(--white); font-family: "Nunito", sans-serif; font-weight: 700; font-size: 21px;
    display: flex; align-items: center; padding-left: 20px; letter-spacing: 0.5px;
  }
  .badge-minding { top: 150px; }
  .badge-minding .badge-photo { background: linear-gradient(160deg, #9ec6d8 0%, #5c5a58 35%, #c08452 55%, #5f8a3a 80%, #3f6a2a 100%); }
  .badge-visits { top: 446px; }
  .badge-visits .badge-photo { background: linear-gradient(180deg, #e9e6e0 0%, #d8d2c8 35%, #b28155 60%, #8a5e3b 100%); }
  .badge-walking { top: 750px; }
  .badge-walking .badge-photo { background: linear-gradient(180deg, #6f8a6a 0%, #4b6a3e 40%, #c7ad8a 60%, #5f8c3e 100%); }
</style>
</head>
<body>
<div class="poster">

  <header class="brand">
    <div class="brand-dot"></div>
    <div>
      <div class="brand-name">Paw Haven</div>
      <div class="brand-tag">PET SERVICES</div>
    </div>
  </header>

  <div class="hero-photo" role="img" aria-label="Golden labrador sitting on the sand looking out over a calm blue sea"></div>
  <div class="info-panel"></div>

  <svg class="headline" viewBox="0 0 560 280" role="img" aria-label="Caring for your dog like family">
    <defs>
      <text id="hl-caring" class="headline-word big" x="38" y="100" font-size="82">Caring</text>
      <text id="hl-for" class="headline-word small" x="150" y="140" font-size="44">for</text>
      <text id="hl-yourdog" class="headline-word big" x="42" y="190" font-size="80">your dog</text>
      <text id="hl-like" class="headline-word small" x="130" y="233" font-size="40">like</text>
      <text id="hl-family" class="headline-word big" x="218" y="250" font-size="96">family</text>
    </defs>
    <g class="headline-outline">
      <use href="#hl-caring"/><use href="#hl-for"/><use href="#hl-yourdog"/><use href="#hl-like"/><use href="#hl-family"/>
    </g>
    <g class="headline-fill">
      <use class="big" href="#hl-caring"/>
      <use class="small" href="#hl-for"/>
      <use class="big" href="#hl-yourdog"/>
      <use class="small" href="#hl-like"/>
      <use class="big" href="#hl-family"/>
    </g>
  </svg>

  <p class="tagline">Western Sydney’s complete dog care service.</p>

  <div class="services">
    <div class="service">
      <div class="service-name">Dog Minding&nbsp;&nbsp;-</div>
      <div class="service-text">Your dog stays in the home of one of our carefully selected minders.Treated like part of the family, they enjoy all the creature comforts they are used to.</div>
    </div>
    <div class="service">
      <div class="service-name">Home Visits&nbsp;&nbsp;&nbsp;&nbsp;-</div>
      <div class="service-text">We visit your dog at your home for feeding, walking and playtime. Short of long visits available.</div>
    </div>
    <div class="service">
      <div class="service-name">Dog Walking&nbsp;&nbsp;-</div>
      <div class="service-text">If you can’t walk your dog for any reason we are here to help. 1/2 hour or hourly walks available.</div>
    </div>
  </div>

  <svg class="burst" viewBox="0 0 180 160">
    <polygon fill="var(--alert-red)" points="90,4 102,20 120,8 126,28 146,22 146,42 168,42 160,62 178,72 162,86 174,104 154,108 158,130 138,128 132,150 114,140 102,158 90,142 76,158 66,140 46,150 42,128 22,130 26,108 6,104 18,86 2,72 20,62 12,42 34,42 34,22 54,28 60,8 78,20"/>
    <g transform="rotate(-24 90 80)" text-anchor="middle">
      <text class="burst-text" x="88" y="48">Contact us</text>
      <text class="burst-text" x="88" y="66">today for a</text>
      <text class="burst-text" x="88" y="84">tailored</text>
      <text class="burst-text" x="88" y="102">package</text>
      <text class="burst-text" x="88" y="120">to meet</text>
      <text class="burst-text" x="88" y="138">your needs.</text>
    </g>
  </svg>

  <div class="call">
    <p class="call-lead">Visit our website or call today</p>
    <p class="call-phone">0412 555 019</p>
  </div>

  <div class="web-links">
    <p class="web-link">www.pawhavenexample.com.au</p>
    <p class="web-link">www.facebook.com/pawhavenexampleau</p>
  </div>
  <div class="footer-band"></div>

  <div class="service-badge badge-minding">
    <div class="badge-photo" role="img" aria-label="Tricolour shepherd dog sitting in the grass"></div>
    <div class="badge-ribbon">Dog Minding</div>
  </div>
  <div class="service-badge badge-visits">
    <div class="badge-photo" role="img" aria-label="Small terrier sitting on a home doormat"></div>
    <div class="badge-ribbon">Home Visits</div>
  </div>
  <div class="service-badge badge-walking">
    <div class="badge-photo" role="img" aria-label="Bulldog on a lead standing on a grassy path"></div>
    <div class="badge-ribbon">Dog Walking</div>
  </div>

</div>
</body>
</html>
```